Fernwillow needs product labels for deodorant line, and future soap, and lip balm line.

Fernwillow is a new startup that at this time is looking for labels for our deodorant line. There will be future work for our other products given to the winning designer. Our products are all-natural free from petrochemicals, propylene glycol, parabens, aluminum compounds, or synthetic colorants. All our products are also handmade.
We are using a standard size stick to contain the product, on the front cap the label is 2"W x 1"H, on the body front and back the size is 2" W x 2.675" H. We want the front to say "aluminum free", and "all-natural deodorant"
The back needs to include, a UPC, Our mission is to bring you effective, all-natural products using the highest quality ingredients. , Ingredients Cocoa Butter, Shea Butter, Arrowroot Powder, Sodium Bicarbonate, Olive Oil, Water.
We are launching 4 scents.
scent free
Lavander
Tea Tree
Baby Powder
We included a couple pics of product labels we like but are definitely not limited to them. also a picture of the empty container.
Updates
Project Deadline Extended
Reason: Someone completed their design but didn't post it in time and asked me to extend the dead line.
Target Market(s)
Females that are health conscience.
Industry/Entity Type
Cosmetics

```html
<!DOCTYPE html>
<html lang="en">
<head>
<meta charset="utf-8">
<title>Fernwillow Tea Tree Deodorant Label</title>
<link href="https://fonts.googleapis.com/css2?family=Open+Sans:wght@400;600;700&display=swap" rel="stylesheet">
<style>
  :root {
    --bg: #eeeff0;
    --ink: #222222;
    --green-deep: #3d8a1e;
    --green-mid: #5aa82a;
    --green-light: #a9d46a;
    --green-pale: #dcefc2;
    --white: #ffffff;
  }
  * { margin: 0; padding: 0; box-sizing: border-box; }
  html, body { width: 1200px; height: 1000px; overflow: hidden; }
  body {
    background: var(--bg);
    font-family: "Open Sans", Arial, sans-serif;
    position: relative;
  }
  .brand-wordmark {
    position: absolute;
    left: 495px;
    top: 62px;
    font-size: 92px;
    font-weight: 700;
    color: var(--ink);
    letter-spacing: -1px;
    line-height: 1;
  }
  .brand-wordmark .tm {
    font-size: 20px;
    font-weight: 400;
    margin-left: 8px;
    letter-spacing: 0;
  }
  .label {
    position: absolute;
    left: 75px;
    top: 240px;
    width: 508px;
    height: 580px;
    border-radius: 8px;
    overflow: hidden;
    background: var(--white);
    box-shadow: 0 2px 8px rgba(0,0,0,0.2);
  }
  .label svg { display: block; }
</style>
</head>
<body>
  <div class="brand-wordmark">Fernwillow<span class="tm">TM</span></div>

  <div class="label">
    <svg width="508" height="580" viewBox="0 0 508 580" xmlns="http://www.w3.org/2000/svg">
      <defs>
        <linearGradient id="leafTones" x1="0" y1="0" x2="1" y2="1">
          <stop offset="0" stop-color="#4f9a22"/>
          <stop offset="0.5" stop-color="#9fd05a"/>
          <stop offset="1" stop-color="#e8f5d6"/>
        </linearGradient>
        <linearGradient id="waveTones" x1="0" y1="0" x2="1" y2="0">
          <stop offset="0" stop-color="#e6f3d6"/>
          <stop offset="0.5" stop-color="#7dbd3c"/>
          <stop offset="1" stop-color="#3d8a1e"/>
        </linearGradient>
        <radialGradient id="dotTones" cx="0.7" cy="0.3" r="0.7">
          <stop offset="0" stop-color="#b6db86"/>
          <stop offset="1" stop-color="#ffffff"/>
        </radialGradient>
        <clipPath id="labelClip"><rect width="508" height="580"/></clipPath>
      </defs>
      <g clip-path="url(#labelClip)">
        <rect class="top-band" x="0" y="0" width="508" height="16" fill="var(--green-mid)"/>

        <rect class="halftone-area" x="300" y="60" width="208" height="200" fill="url(#dotTones)" role="img" aria-label="Halftone green dot texture"/>

        <path class="wave-area" d="M210 290 C 320 200, 420 210, 508 180 L 508 500 C 420 470, 360 420, 300 410 Z" fill="url(#waveTones)" role="img" aria-label="Flowing green wave ribbons"/>

        <circle class="leaf-photo" cx="170" cy="330" r="225" fill="url(#leafTones)" role="img" aria-label="Photo of fresh green leaves on a branch"/>

        <circle class="scent-disc" cx="110" cy="445" r="215" fill="var(--green-deep)" opacity="0.95"/>
        <circle cx="110" cy="445" r="215" fill="none" stroke="var(--green-light)" stroke-width="6" opacity="0.6"/>

        <text class="label-brand" x="125" y="100" font-family="Open Sans, Arial, sans-serif" font-size="46" font-weight="700" fill="var(--ink)">Fernwillow</text>
        <text x="450" y="112" font-family="Open Sans, Arial, sans-serif" font-size="13" fill="var(--ink)">TM</text>

        <g class="claim-badge">
          <circle cx="330" cy="255" r="64" fill="var(--green-deep)" stroke="var(--green-pale)" stroke-width="3"/>
          <text x="330" y="240" text-anchor="middle" font-size="17" fill="var(--white)">all skin types</text>
          <text x="330" y="260" text-anchor="middle" font-size="17" fill="var(--white)">+</text>
          <text x="330" y="281" text-anchor="middle" font-size="17" fill="var(--white)">aluminum</text>
          <text x="330" y="302" text-anchor="middle" font-size="17" fill="var(--white)">free</text>
        </g>

        <text class="scent-name" x="40" y="463" font-size="32" font-weight="600" fill="var(--white)" letter-spacing="1">TEA TREE</text>
        <line x1="40" y1="472" x2="290" y2="472" stroke="var(--green-pale)" stroke-width="1.2"/>
        <text class="product-type" x="40" y="494" font-size="19" fill="var(--green-pale)">All-Natural Deodorant</text>

        <text class="net-weight" x="482" y="525" text-anchor="end" font-family="Arial, sans-serif" font-size="17" fill="#111">NET WT 60g</text>
        <text x="478" y="552" text-anchor="end" font-family="Arial, sans-serif" font-size="17" fill="#111">(12.3 OZ)</text>
      </g>
    </svg>
  </div>
</body>
</html>
```